Varnel Supply requires a new business card.

We are an online professional tool store.

Target Market(s)

We target the professional technician.

Industry/Entity Type

Business

Contact Information for Business Card

VarnelSupply.com.au

sales@varnelsupply.example

Requirements
Must have
• Needs to look commercial and professional
Should not have
• No Australian Colors, maps or shapes.
• No Shapes of Tools

```html
<!DOCTYPE html>
<html lang="en">
<head>
<meta charset="utf-8">
<title>Varnel Supply — Business Card</title>
<link rel="stylesheet" href="https://fonts.googleapis.com/css2?family=Open+Sans:wght@400;600;700&display=swap">
<style>
  :root {
    --backdrop: #2a2b2e;
    --card-white: #ffffff;
    --brand-blue: #1a2fb0;
    --brand-blue-deep: #0f27a8;
    --brand-cyan: #129bd4;
    --front-top: #0a8fd0;
    --front-bottom: #0d2fb5;
    --ink: #222222;
    --ink-soft: #444444;
  }
  * { margin: 0; padding: 0; box-sizing: border-box; }
  html, body { width: 1200px; height: 864px; overflow: hidden; }
  body {
    background: var(--backdrop);
    font-family: "Open Sans", Arial, sans-serif;
    position: relative;
  }
  .card {
    position: absolute;
    left: 320px;
    width: 560px;
    height: 320px;
    border-radius: 3px;
    overflow: hidden;
  }
  .card--front {
    top: 72px;
    background: linear-gradient(170deg, var(--front-top) 0%, #0b62c8 45%, var(--front-bottom) 100%);
  }
  .card--back {
    top: 472px;
    background: var(--card-white);
  }
  .front-wordmark {
    position: absolute;
    right: 70px;
    top: 126px;
    color: var(--card-white);
    font-weight: 700;
    font-size: 46px;
    line-height: 1;
    letter-spacing: 0.5px;
  }
  .holder {
    position: absolute;
    left: 38px;
    top: 120px;
  }
  .holder-name {
    color: var(--brand-blue);
    font-weight: 700;
    font-size: 19px;
    line-height: 1.2;
  }
  .holder-title {
    color: var(--ink-soft);
    font-size: 12px;
    line-height: 1.3;
  }
  .back-wordmark {
    position: absolute;
    right: 44px;
    top: 92px;
    display: flex;
    align-items: center;
    gap: 10px;
    color: var(--brand-blue-deep);
    font-weight: 700;
    font-size: 32px;
    line-height: 1;
  }
  .back-wordmark .mark-dot {
    width: 18px;
    height: 18px;
    border-radius: 50%;
    background: var(--brand-cyan);
  }
  .contact-list {
    position: absolute;
    right: 28px;
    bottom: 24px;
    list-style: none;
    text-align: right;
  }
  .contact-list li {
    display: flex;
    justify-content: flex-end;
    align-items: center;
    gap: 10px;
    color: var(--ink);
    font-size: 13.5px;
    line-height: 22px;
  }
  .contact-list svg {
    width: 12px;
    height: 12px;
    fill: var(--brand-blue);
    flex: none;
  }
</style>
</head>
<body>

  <section class="card card--front" aria-label="Business card front">
    <div class="front-wordmark">Varnel Supply</div>
  </section>

  <section class="card card--back" aria-label="Business card back">
    <div class="holder">
      <p class="holder-name">Dorian Keller</p>
      <p class="holder-title">Managing Director</p>
    </div>

    <div class="back-wordmark">
      <span class="mark-dot" aria-hidden="true"></span>
      <span>Varnel Supply</span>
    </div>

    <ul class="contact-list">
      <li>044-555-0192
        <svg viewBox="0 0 12 12" aria-hidden="true"><path d="M2.5 0.8l2 2.2-1 1.3c.7 1.5 1.8 2.6 3.3 3.3l1.3-1 2.2 2-1.2 1.9C5.6 10.4 1.6 6.4 0.6 2z"/></svg>
      </li>
      <li>123-555-0147
        <svg viewBox="0 0 12 12" aria-hidden="true"><rect x="3" y="1" width="6" height="3"/><rect x="1" y="4.5" width="10" height="6.5" rx="1"/></svg>
      </li>
      <li>123-555-0147
        <svg viewBox="0 0 12 12" aria-hidden="true"><path d="M3.5 0.5h5a1 1 0 0 1 1 1v9a1 1 0 0 1-1 1h-5a1 1 0 0 1-1-1v-9a1 1 0 0 1 1-1zm.5 1.5v7h4V2z"/></svg>
      </li>
      <li>sales@varnelsupply.example
        <svg viewBox="0 0 12 12" aria-hidden="true"><path d="M0.5 2.5h11v7h-11z M1 3l5 3.5L11 3" stroke="#fff" stroke-width="0.8"/></svg>
      </li>
      <li>www.varnelsupply.example
        <svg viewBox="0 0 12 12" aria-hidden="true"><path d="M5 7l2-2M4.3 5.5L2.6 7.2a1.8 1.8 0 0 0 2.5 2.5l1.7-1.7M7.7 6.5l1.7-1.7a1.8 1.8 0 0 0-2.5-2.5L5.2 4" fill="none" stroke="#1a2fb0" stroke-width="1.3" stroke-linecap="round"/></svg>
      </li>
    </ul>
  </section>

</body>
</html>
```